Guitar parts retail packaging

I have 2 boxes I need designed. This will be for my guitar parts. They are going to be thick cardstock type paper box, with a foam insert to secure the items. Matte finish with silver foil printing is sort of where im headed, but Im open to other beautiful design. The boxes will need to have a window on top of the box to show the product inside. Color scheme Im thinking with is Black with red, white and Silver foil printing. Unless you come up with something nicer, im open to that. But my business cards and some stickers are those colors.
2 different size boxes, but they can be the same basic design, modified for 2 different sizes. They will open at the front, and the lid will lift, hinged at the top back edge. (Please see purple box in picture for example for how box will work). Both boxes will have a window on top to showcase product in the box. One of the sides, (2" X 1.25") will be left a solid color, grey or other so I can put a product sticker on that side to designate what type of product is in the box. So you are really just designing the top (With window), front, back, and 1 side. Maybe something clever on the bottom but if thats blank thats fine.
LARGE BOX:
5.25 wide (Left to right)
2” deep (Front to back)
1.25” tall (Top to bottom)
SMALL BOX:
2” Wide (Left to right)
2” Deep (Front to back)
Please see Business card and sticker in picture for color scheme Im thinking. ( I am open to other colors and designs as well)

Target Market(s)

Musicians, Rockers, tattoo junkies, general badasses.

Industry/Entity Type

Guitar industry. Rock & Rollers

Font styles to use
Other font styles liked:
• I use a font called Morpheus for my logo. Also Times New Roman, maybe Copperplate? Or something more creative? Im open as long as it fits.

Colors
EB3D1F
EC4F4E
F09395
F8D3D4
FCEDEE

Requirements
Must have
• My Company name and logo (Harrow Kestrel). Also slogan-
Nice to have
• Please see general aesthetic in sticker and biz card.
Should not have
• No horror themes, keep it cool and classy. (Even though logo is a skull). And please no pictures of guitars on the box. You might add a pic of 1 type of guitar, but the parts inside might not fit that guitar pictured on the box.

```html
<!DOCTYPE html>
<html lang="en">
<head>
<meta charset="utf-8">
<title>Harrow Kestrel — Large Parts Box</title>
<link rel="stylesheet" href="https://fonts.googleapis.com/css2?family=Cinzel:wght@500&display=swap">
<style>
  :root {
    --bg: #e4e4e4;
    --red-bright: #c10f14;
    --red-mid: #9c0c0b;
    --red-deep: #6e0904;
    --red-shade: #560603;
    --silver: #e6e6ea;
    --silver-edge: #b9b9c2;
    --window: #bdbbbb;
    --brand-font: "Cinzel", serif;
  }
  html, body {
    margin: 0;
    padding: 0;
    width: 1200px;
    height: 800px;
    overflow: hidden;
    background: var(--bg);
  }
  .canvas {
    position: relative;
    width: 1200px;
    height: 800px;
  }
  .panel {
    position: absolute;
    overflow: hidden;
  }
  .panel-fill {
    position: absolute;
    inset: 0;
  }
  .panel--top {
    left: 372px; top: 172px; width: 735px; height: 280px;
  }
  .panel--top .panel-fill {
    background: linear-gradient(160deg, var(--red-bright) 0%, var(--red-mid) 60%, var(--red-deep) 100%);
  }
  .panel--front {
    left: 372px; top: 452px; width: 735px; height: 175px;
  }
  .panel--front .panel-fill {
    background: linear-gradient(180deg, var(--red-mid) 0%, var(--red-deep) 100%);
  }
  .panel--side {
    left: 92px; top: 452px; width: 280px; height: 175px;
  }
  .panel--side .panel-fill {
    background: linear-gradient(90deg, var(--red-shade) 0%, var(--red-deep) 100%);
  }
  .fold-line {
    position: absolute;
    background: rgba(0,0,0,0.25);
  }
  .fold-line--top-front { left: 372px; top: 451px; width: 735px; height: 1px; }
  .fold-line--side-front { left: 371px; top: 452px; width: 1px; height: 175px; }

  .top-art {
    position: absolute;
    inset: 0;
  }
  .brand-name {
    position: absolute;
    margin: 0;
    font-family: var(--brand-font);
    font-weight: 500;
    color: var(--silver);
    white-space: nowrap;
    letter-spacing: 0.02em;
  }
  .brand-name--top {
    left: 82px; top: 28px;
    font-size: 24px;
  }
  .brand-name--front {
    left: 50%; top: 50%;
    transform: translate(-50%, -50%);
    font-size: 46px;
  }
  .brand-name--side {
    left: 50%; top: 50%;
    transform: translate(-50%, -50%) rotate(-90deg);
    font-size: 18px;
  }
</style>
</head>
<body>
<main class="canvas">

  <section class="panel panel--top" aria-label="Box lid">
    <div class="panel-fill" role="img" aria-label="Deep red background with darker red flowing swirl pattern"></div>
    <svg class="top-art" width="735" height="280" viewBox="0 0 735 280">
      <rect class="window-frame" x="150" y="78" width="520" height="120" rx="18" fill="var(--silver-edge)"/>
      <rect class="window-opening" x="155" y="83" width="510" height="110" rx="15" fill="var(--window)"/>
      <g class="rule-lines" stroke="var(--silver)" stroke-width="2">
        <line x1="330" y1="226" x2="520" y2="226"/>
        <line x1="340" y1="233" x2="520" y2="233"/>
        <line x1="350" y1="240" x2="520" y2="240"/>
        <line x1="545" y1="226" x2="690" y2="226"/>
        <line x1="545" y1="233" x2="680" y2="233"/>
        <line x1="545" y1="240" x2="670" y2="240"/>
      </g>
    </svg>
    <p class="brand-name brand-name--top">Harrow Kestrel</p>
  </section>

  <section class="panel panel--front" aria-label="Box front">
    <div class="panel-fill" role="img" aria-label="Dark red background with flowing swirl pattern"></div>
    <h1 class="brand-name brand-name--front">Harrow Kestrel</h1>
  </section>

  <section class="panel panel--side" aria-label="Box side">
    <div class="panel-fill" role="img" aria-label="Shaded dark red background with flowing swirl pattern"></div>
    <p class="brand-name brand-name--side">Harrow Kestrel</p>
  </section>

  <div class="fold-line fold-line--top-front"></div>
  <div class="fold-line fold-line--side-front"></div>
</main>
</body>
</html>
```